Civic Learning Studio PocketDeck

We are looking for a fresh new look for our famous Signal Sense Handset cards. These cards are used as a pedagogical device by teachers and students to help people critically analyze media messages.

Now that we are in the era of Orvo 12, we would like the Signal Sense Handset to look fresh and new. All the content stays the same, but graphic elements, color and overall design can be changed to look contemporary and modern.

Target Market(s)

Teenagers, young adults, secondary and college teachers

Industry/Entity Type

Education

Colors

Designer to choose colors to be used in the design.

Requirements
Must have
• All the content that is on the current card, with icons and text
Nice to have
• Fresh use of color
• More modern phone design like the smartphones people use today
Should not have
• ...too much black

```html
<!DOCTYPE html>
<html lang="en">
<head>
<meta charset="utf-8">
<title>Signal Sense Handset — PocketDeck</title>
<link href="https://fonts.googleapis.com/css2?family=Arimo:wght@400;700&display=swap" rel="stylesheet">
<style>
  :root{
    --teal:#14a89c; --teal-deep:#0b6159;
    --ink:#000; --white:#fff; --text-dark:#1a2a33;
    --blue:#1f9fbd; --green:#8cc63f; --yellow:#f7c21b; --orange:#f15a29;
    --row-blue:#dce3e8; --row-green:#e3e6d8; --row-yellow:#ebe4d8; --row-orange:#ecdcd6;
  }
  *{box-sizing:border-box;margin:0;padding:0}
  html,body{width:1200px;height:1200px;overflow:hidden}
  body{font-family:"Arimo",Arial,sans-serif;background:linear-gradient(var(--teal) 0 920px,var(--teal-deep) 920px 1200px);position:relative}
  .screen{position:absolute;top:148px;width:406px;height:888px;border-radius:40px;overflow:hidden}
  .screen--questions{left:138px;background:var(--ink)}
  .screen--discuss{left:656px}
  .screen__photo{position:absolute;inset:0;background:linear-gradient(160deg,#3c4a3a 0%,#6d7a78 45%,#8a8f99 70%,#5b6470 100%)}
  .screen__shade{position:absolute;left:0;right:0;top:0;height:452px;background:rgba(0,0,0,.55)}
  .screen__fade{position:absolute;left:0;right:0;top:452px;bottom:0;background:rgba(0,0,0,.2)}
  .el{position:absolute}
  .rule{position:absolute;left:8px;right:8px;height:6px;border-top:2px solid var(--white);border-bottom:2px solid var(--white)}
  .title{position:absolute;left:0;right:0;text-align:center;color:var(--white);font-weight:700;text-transform:uppercase;line-height:1.18}
  .questions__title{top:90px;font-size:32px}
  .question{position:absolute;left:8px;width:385px;height:70px;display:flex}
  .question__num{width:29px;display:flex;align-items:center;justify-content:center;font-weight:700;font-size:17px;color:var(--text-dark)}
  .question__text{flex:1;padding:0 10px 0 12px;display:flex;align-items:center;font-weight:700;font-size:17.5px;line-height:1.3;color:var(--text-dark)}
  .brand{position:absolute;left:0;right:0;top:762px;text-align:center;color:var(--white)}
  .brand__name{font-size:26px;font-weight:700;display:inline-flex;align-items:center;gap:10px}
  .brand__mark{width:16px;height:16px;background:var(--orange)}
  .brand__url{display:block;margin-top:4px;font-size:15px;text-decoration:underline}
  .discuss__title{top:106px;font-size:34px;text-transform:uppercase}
  .tile{position:absolute;display:flex;align-items:center;justify-content:center;border-radius:4px}
  .tile--prompt{width:68px;height:68px}
  .tile--media{width:70px;height:70px;background:var(--white);border-radius:6px}
  .tile svg{width:48px;height:48px}
  .label{position:absolute;width:100px;text-align:center;color:var(--white);font-weight:700;font-size:13.6px;line-height:1.15}
</style>
</head>
<body>

<section class="screen screen--questions">
  <div class="rule" style="top:84px"></div>
  <h1 class="title questions__title">Key Questions of<br>Media Literacy</h1>
  <div class="rule" style="top:172px"></div>

  <div class="question" style="top:229px;background:var(--row-blue)"><span class="question__num" style="background:var(--blue)">1</span><p class="question__text">Who is the author and what is the purpose?</p></div>
  <div class="question" style="top:314px;background:var(--row-green)"><span class="question__num" style="background:var(--green)">2</span><p class="question__text">What techniques are used to attract and hold your attention?</p></div>
  <div class="question" style="top:399px;background:var(--row-yellow)"><span class="question__num" style="background:var(--yellow)">3</span><p class="question__text">What lifestyles, values and points of view are represented?</p></div>
  <div class="question" style="top:484px;background:var(--row-orange)"><span class="question__num" style="background:var(--orange)">4</span><p class="question__text">How might different people interpret the message?</p></div>
  <div class="question" style="top:570px;background:var(--row-blue)"><span class="question__num" style="background:var(--blue)">5</span><p class="question__text">What is omitted from the message?</p></div>

  <div class="brand">
    <div class="brand__name"><span class="brand__mark"></span>Civic Learning Studio</div>
    <span class="brand__url">www.civiclearningstudio.org</span>
  </div>
</section>

<section class="screen screen--discuss">
  <div class="screen__photo" role="img" aria-label="Photo of smiling students gathered around a laptop"></div>
  <div class="screen__shade"></div>
  <div class="screen__fade"></div>

  <div class="rule" style="top:94px"></div>
  <h2 class="title discuss__title">Time to Discuss</h2>
  <div class="rule" style="top:152px"></div>

  <!-- discussion prompts -->
  <div class="tile tile--prompt" style="left:26px;top:187px;background:var(--blue)"><svg viewBox="0 0 48 48"><path d="M8 25l10 10 22-22" fill="none" stroke="#fff" stroke-width="7" stroke-linecap="round" stroke-linejoin="round"/></svg></div>
  <div class="tile tile--prompt" style="left:123px;top:187px;background:var(--green)"><svg viewBox="0 0 48 48"><path d="M19 6h10l-3 8h-4z" fill="#fff"/><path d="M20 15h8c8 6 12 14 12 21 0 5-4 7-16 7S8 41 8 36c0-7 4-15 12-21z" fill="#fff"/><text x="24" y="37" text-anchor="middle" font-size="17" font-weight="700" fill="#8cc63f" font-family="Arimo,sans-serif">$</text></svg></div>
  <div class="tile tile--prompt" style="left:220px;top:187px;background:var(--yellow)"><svg viewBox="0 0 48 48"><text x="24" y="41" text-anchor="middle" font-size="44" font-weight="700" fill="#fff" font-family="Arimo,sans-serif">?</text></svg></div>
  <div class="tile tile--prompt" style="left:316px;top:187px;background:var(--orange)"><svg viewBox="0 0 48 48"><path d="M14 8h20l9 11-19 23L5 19z" fill="none" stroke="#fff" stroke-width="3.5" stroke-linejoin="round"/><path d="M5 19h38M19 8l-4 11 9 23 9-23-4-11" fill="none" stroke="#fff" stroke-width="3"/></svg></div>

  <div class="label" style="left:10px;top:267px">Reality<br>Check</div>
  <div class="label" style="left:107px;top:267px;width:110px">Private Gain or<br>Public Good?</div>
  <div class="label" style="left:204px;top:267px">What's<br>Left Out?</div>
  <div class="label" style="left:300px;top:267px">Values<br>Check</div>

  <div class="tile tile--prompt" style="left:26px;top:320px;background:var(--orange)"><svg viewBox="0 0 48 48"><path d="M3 24c6-9 13-13 21-13s15 4 21 13c-6 9-13 13-21 13S9 33 3 24z" fill="#fff"/><circle cx="24" cy="24" r="9" fill="#f15a29"/><circle cx="24" cy="24" r="4.5" fill="#fff"/></svg></div>
  <div class="tile tile--prompt" style="left:123px;top:320px;background:var(--yellow)"><svg viewBox="0 0 48 48"><path d="M24 5c-9 0-13 7-13 15v10l-5 6h36l-5-6V20c0-8-4-15-13-15z" fill="#fff"/><path d="M18 39a6 6 0 0 0 12 0z" fill="#fff"/></svg></div>
  <div class="tile tile--prompt" style="left:220px;top:320px;background:var(--green)"><svg viewBox="0 0 48 48"><path d="M24 5L45 43H3z" fill="#fff"/><rect x="22" y="17" width="4" height="15" fill="#8cc63f"/><circle cx="24" cy="37" r="2.5" fill="#8cc63f"/></svg></div>
  <div class="tile tile--prompt" style="left:316px;top:320px;background:var(--blue)"><svg viewBox="0 0 48 48"><path d="M30 6l8 8-20 20-10 2 2-10z" fill="#fff"/><rect x="6" y="41" width="36" height="3" fill="#fff"/></svg></div>

  <div class="label" style="left:4px;top:400px;width:112px">Read Between<br>the Lines</div>
  <div class="label" style="left:107px;top:400px">Stereotype<br>Alert</div>
  <div class="label" style="left:204px;top:400px">Solutions<br>too Easy</div>
  <div class="label" style="left:300px;top:400px;width:104px">Record/Save<br>for Later</div>

  <!-- media types -->
  <div class="tile tile--media" style="left:25px;top:498px"><svg viewBox="0 0 48 48"><path d="M6 6h32v36H8a4 4 0 0 1-4-4V14h2z" fill="none" stroke="#000" stroke-width="3"/><rect x="11" y="11" width="12" height="12" fill="#000"/><path d="M11 28h22M11 33h22M11 38h22M27 13h6M27 19h6" stroke="#000" stroke-width="2.5"/></svg></div>
  <div class="tile tile--media" style="left:123px;top:498px"><svg viewBox="0 0 48 48"><rect x="9" y="9" width="30" height="22" rx="2" fill="none" stroke="#000" stroke-width="3"/><path d="M4 35h40l-3 5H7z" fill="#000"/><path d="M21 14v12l3-3 3 5 2-1-3-5h4z" fill="#000"/></svg></div>
  <div class="tile tile--media" style="left:223px;top:498px"><svg viewBox="0 0 48 48"><path d="M16 4l8 8 8-8" fill="none" stroke="#000" stroke-width="3"/><rect x="4" y="13" width="40" height="28" rx="3" fill="none" stroke="#000" stroke-width="3"/><rect x="9" y="18" width="24" height="18" fill="#000"/><circle cx="38" cy="22" r="2" fill="#000"/><circle cx="38" cy="30" r="2" fill="#000"/></svg></div>
  <div class="tile tile--media" style="left:322px;top:498px"><svg viewBox="0 0 48 48"><path d="M5 9l36-4 1 6-36 4z" fill="#000"/><rect x="6" y="17" width="36" height="26" fill="#000"/><circle cx="24" cy="30" r="8" fill="#fff"/><path d="M22 26v8l6-4z" fill="#000"/></svg></div>

  <div class="label" style="left:10px;top:580px">News Media</div>
  <div class="label" style="left:108px;top:580px">Websites</div>
  <div class="label" style="left:208px;top:580px">TV</div>
  <div class="label" style="left:307px;top:580px">Movies</div>

  <div class="tile tile--media" style="left:25px;top:614px"><svg viewBox="0 0 48 48"><circle cx="24" cy="24" r="19" fill="none" stroke="#000" stroke-width="4"/><g fill="#000"><rect x="14" y="16" width="5" height="6"/><rect x="21.5" y="16" width="5" height="6"/><rect x="29" y="16" width="5" height="6"/><rect x="14" y="25" width="5" height="6"/><rect x="21.5" y="25" width="5" height="6"/><rect x="29" y="25" width="5" height="6"/></g></svg></div>
  <div class="tile tile--media" style="left:123px;top:614px"><svg viewBox="0 0 48 48"><g fill="none" stroke="#000" stroke-width="3" stroke-linecap="round"><path d="M10 32a17 17 0 1 1 28 0"/><path d="M16 28a10 10 0 1 1 16 0"/></g><circle cx="24" cy="20" r="5" fill="#000"/><rect x="21" y="26" width="6" height="18" rx="3" fill="#000"/></svg></div>
  <div class="tile tile--media" style="left:223px;top:614px"><svg viewBox="0 0 48 48"><path d="M4 8h40v26H24l-8 8v-8H4z" fill="#000"/><circle cx="15" cy="21" r="3" fill="#fff"/><circle cx="24" cy="21" r="3" fill="#fff"/><circle cx="33" cy="21" r="3" fill="#fff"/></svg></div>
  <div class="tile tile--media" style="left:322px;top:614px"><svg viewBox="0 0 48 48"><path d="M4 14l20-6 20 10-20 8z" fill="#000"/><path d="M8 22l16 8 16-7v8l-16 8-16-8z" fill="none" stroke="#000" stroke-width="3"/><path d="M30 30v12l3-2 3 2V28" fill="#000"/></svg></div>

  <div class="label" style="left:10px;top:694px">Apps</div>
  <div class="label" style="left:108px;top:694px">Podcasts</div>
  <div class="label" style="left:208px;top:694px">Comics</div>
  <div class="label" style="left:307px;top:694px">Books</div>

  <div class="tile tile--media" style="left:25px;top:726px"><svg viewBox="0 0 48 48"><path d="M16 8l24-4v28" fill="none" stroke="#000" stroke-width="4"/><path d="M16 8v28" stroke="#000" stroke-width="4"/><path d="M16 8l24-4v7l-24 4z" fill="#000"/><ellipse cx="11" cy="37" rx="6" ry="5" fill="#000"/><ellipse cx="35" cy="33" rx="6" ry="5" fill="#000"/></svg></div>
  <div class="tile tile--media" style="left:123px;top:726px"><svg viewBox="0 0 48 48"><path d="M14 24l20-11M14 24l20 11" stroke="#000" stroke-width="4"/><circle cx="13" cy="24" r="7" fill="#000"/><circle cx="35" cy="12" r="7" fill="#000"/><circle cx="35" cy="36" r="7" fill="#000"/></svg></div>
  <div class="tile tile--media" style="left:223px;top:726px"><svg viewBox="0 0 48 48"><path d="M12 14h24c5 0 8 4 9 10l1 10c0 4-4 6-7 2l-5-5H14l-5 5c-3 4-7 2-7-2l1-10c1-6 4-10 9-10z" fill="#000"/><path d="M10 22h8M14 18v8" stroke="#fff" stroke-width="2.5"/><circle cx="32" cy="20" r="2" fill="#fff"/><circle cx="37" cy="24" r="2" fill="#fff"/></svg></div>
  <div class="tile tile--media" style="left:322px;top:726px"><svg viewBox="0 0 48 48"><path d="M15 12a16 16 0 1 0 18 0" fill="none" stroke="#000" stroke-width="5" stroke-linecap="round"/><path d="M24 4v18" stroke="#000" stroke-width="5" stroke-linecap="round"/></svg></div>

  <div class="label" style="left:10px;top:806px">Music</div>
  <div class="label" style="left:103px;top:806px;width:110px">Social Media</div>
  <div class="label" style="left:203px;top:806px;width:110px">Video Games</div>
  <div class="label" style="left:307px;top:806px">Off</div>
</section>

</body>
</html>
```